Wholesale in Gold Jewellery & Gold Bullion

We are an established gold jewellery and gold bullion wholesaler selling these products to international clients. We already have a name and logo of our company, hence please view attached current card design. We need a completely new design to compliment our business and industry and the final design should be new and elegant.

Contact Information for Business Card

New card details must be same as per current card. Like logo, name, tel no. & etc.

Colors

Designer to choose colors to be used in the design.

```html
<!DOCTYPE html>
<html lang="en">
<head>
<meta charset="utf-8">
<title>Arven &amp; Co — Business Card</title>
<link href="https://fonts.googleapis.com/css2?family=Source+Serif+4:opsz,wght@8..60,400;8..60,600;8..60,700&display=swap" rel="stylesheet">
<style>
  :root {
    --backdrop: #cccccc;
    --card-dark: #1a1a1a;
    --card-light: #ffffff;
    --gold: #f0b53c;
    --ink: #1a1a1a;
  }
  * { margin: 0; padding: 0; box-sizing: border-box; }
  html, body { width: 1200px; height: 1200px; overflow: hidden; }
  body {
    background: var(--backdrop);
    font-family: "Source Serif 4", Georgia, serif;
    color: var(--ink);
    position: relative;
  }
  .card {
    position: absolute;
    left: 210px;
    width: 778px;
    height: 446px;
    border-radius: 26px;
  }
  .card--front { top: 140px; background: var(--card-dark); }
  .card--back { top: 622px; background: var(--card-light); }

  .brand-mark {
    position: absolute;
    border-radius: 50%;
  }
  .card--front .brand-mark {
    left: 349px; top: 134px;
    width: 80px; height: 80px;
    border: 4px solid var(--gold);
  }
  .card--front .brand-name {
    position: absolute;
    left: 0; right: 0; top: 262px;
    text-align: center;
    font-size: 32px;
    font-weight: 600;
    color: var(--gold);
    letter-spacing: 0.3px;
  }

  .holder { position: absolute; left: 58px; top: 56px; }
  .holder-name {
    font-size: 37px; font-weight: 700; line-height: 1.1; letter-spacing: 0.2px;
  }
  .holder-role { font-size: 32px; font-weight: 400; line-height: 1.2; }

  .card--back .brand-mark {
    left: 584px; top: 54px;
    width: 76px; height: 76px;
    border: 4px solid var(--gold);
  }
  .card--back .brand-name {
    position: absolute;
    left: 512px; width: 220px; top: 151px;
    text-align: center;
    font-size: 18px; font-weight: 600;
  }

  .contact {
    position: absolute;
    display: flex; align-items: center; gap: 12px;
    font-size: 18px; line-height: 1;
  }
  .contact svg { width: 27px; height: 27px; fill: var(--ink); flex: none; }
  .contact--phone { left: 58px; top: 225px; }
  .contact--fax { left: 58px; top: 270px; }
  .contact--mobile { left: 58px; top: 318px; }
  .contact--email { left: 58px; top: 364px; }
  .contact--address { left: 388px; top: 364px; }
  .contact--address svg { width: 24px; height: 27px; }
</style>
</head>
<body>
  <section class="card card--front">
    <div class="brand-mark"></div>
    <div class="brand-name">ARVEN &amp; CO PTE LTD</div>
  </section>

  <section class="card card--back">
    <div class="holder">
      <div class="holder-name">RAVINDER KOLATHAN</div>
      <div class="holder-role">Director</div>
    </div>

    <div class="brand-mark"></div>
    <div class="brand-name">ARVEN &amp; CO PTE LTD</div>

    <div class="contact contact--phone">
      <svg viewBox="0 0 24 24"><path d="M6.6 10.8c1.4 2.8 3.8 5.1 6.6 6.6l2.2-2.2c.3-.3.7-.4 1-.2 1.1.4 2.3.6 3.6.6.6 0 1 .4 1 1V20c0 .6-.4 1-1 1C10.6 21 3 13.4 3 4c0-.6.4-1 1-1h3.5c.6 0 1 .4 1 1 0 1.3.2 2.5.6 3.6.1.3 0 .7-.2 1L6.6 10.8z"/></svg>
      <span>+65 6120 4500</span>
    </div>
    <div class="contact contact--fax">
      <svg viewBox="0 0 24 24"><path d="M7 2h10v5H7z"/><path d="M4 8h16a2 2 0 0 1 2 2v7h-4v-3H6v3H2v-7a2 2 0 0 1 2-2z"/><path d="M7 15h10v7H7zM9 17v1h6v-1zM9 19v1h6v-1z" fill-rule="evenodd"/></svg>
      <span>+65 6384 2219</span>
    </div>
    <div class="contact contact--mobile">
      <svg viewBox="0 0 24 24"><path d="M2 5h20v14H2zM4 7v.4l8 6 8-6V7zm0 2.9V17l4.7-3.6zm16 0-4.7 3.5L20 17zM10.3 14.6 4.8 17h14.4l-5.5-2.4L12 16z" fill-rule="evenodd"/></svg>
      <span>+65 9153 8842</span>
    </div>
    <div class="contact contact--email">
      <svg viewBox="0 0 24 24"><path d="M12 1 2 9v13h20V9zm0 2.5L19.5 9 18 10.1V5H6v5.1L4.5 9zM8 7h8v4.6l-4 3-4-3zM4 11l6 4.5L4 20zm16 0v9l-6-4.5zM12 17l6.5 3.5h-13z" fill-rule="evenodd"/><circle cx="12" cy="9" r="1.8"/></svg>
      <span>ravinder@arvenco.com</span>
    </div>
    <div class="contact contact--address">
      <svg viewBox="0 0 20 24"><path d="M10 0a8 8 0 0 0-8 8c0 6 8 16 8 16s8-10 8-16a8 8 0 0 0-8-8zm0 11a3 3 0 1 1 0-6 3 3 0 0 1 0 6z"/></svg>
      <span>52 Lorong Tembaga, Singapore 208861</span>
    </div>
  </section>
</body>
</html>
```